If everything digital fails, here's what to do

Hi, I would like a poster / infographic of a list of practical actions people could take in case the internet stops working. I've put together a list of 8 areas, with the situation for each, and the mitigation actions folks can take - I need it presented in a clear and aesthetically pleasing way. I will send you the file with the full text so you can include it all

General population, but likely people who are safety conscious and want to protect themselves and learn more about what to do to be tech literate and prepared

Tech / Cyber / Public safety / Civic tech

Sans Serif

• It's a lot of text, so I think the important thing is to have it all in one poster, or in a series of similar pages
• I would like it to be a bit brooding, but also elicit competence and that some experts have thought about this and it will all be okay
• I don't want it to look cartoonish, or cheap - less is more is sort of what I'm looking for

```html
<!DOCTYPE html>
<html lang="en">
<head>
<meta charset="utf-8">
<title>If everything digital fails – Banking &amp; Transportation</title>
<link rel="stylesheet" href="https://fonts.googleapis.com/css2?family=Barlow:wght@700&family=Barlow+Semi+Condensed:wght@400;500;600&family=Barlow+Condensed:wght@600&display=swap">
<style>
:root{
  --ink-teal:#215a65;
  --bright-teal:#43b1b8;
  --curl-teal:#1f7a7a;
  --action-blue:#4a76bf;
  --note-bg:#e1eaf7;
  --text-dark:#23495a;
  --white:#ffffff;
}
*{margin:0;padding:0;box-sizing:border-box}
html,body{width:848px;height:1200px;overflow:hidden;background:var(--white)}
body{position:relative;font-family:"Barlow Semi Condensed",sans-serif}
.abs{position:absolute}

.section-band{position:absolute;left:131px;right:0;height:71px;background:var(--ink-teal);
  font-family:"Barlow",sans-serif;font-weight:700;color:var(--white);
  display:flex;align-items:center;justify-content:center;letter-spacing:1px}
.section-icon{position:absolute;width:108px;height:108px;border-radius:50%;background:var(--ink-teal);
  display:flex;align-items:center;justify-content:center}
.section-icon .disc{width:92px;height:92px;border-radius:50%;background:var(--white);
  display:flex;align-items:center;justify-content:center}

.situation{position:absolute;left:112px;width:620px;background:var(--bright-teal);
  clip-path:polygon(0 0,96% 0,100% 50%,96% 100%,0 100%);
  font-family:"Barlow Condensed",sans-serif;font-weight:600;color:var(--white);
  text-align:center;font-size:18px;line-height:23px;text-shadow:1px 1px 1px rgba(0,0,0,.45);
  display:flex;align-items:center;justify-content:center;padding:0 40px 6px}
.curl{position:absolute;left:112px;width:40px;height:17px;background:var(--curl-teal);border-radius:9px 0 0 9px}
.tab{position:absolute;height:37px;width:194px;color:var(--white);
  font-family:"Barlow Condensed",sans-serif;font-weight:600;font-size:26px;
  display:flex;align-items:center;justify-content:center;text-shadow:1px 1px 1px rgba(0,0,0,.35)}
.tab-do{left:140px;background:var(--ink-teal)}
.tab-refresh{left:506px;background:var(--action-blue)}

.card{position:absolute;border-radius:13px;padding:8px 10px}
.card-do{left:54px;width:389px;background:var(--ink-teal)}
.card-refresh{left:452px;width:346px;background:var(--action-blue)}
.card .inner{height:100%;border-radius:8px;padding:8px 10px;font-size:17.5px;line-height:23.3px}
.card-do .inner{background:linear-gradient(#29515f,#8e9aa3);color:var(--white)}
.card-refresh .inner{background:linear-gradient(#ffffff,#84bcd6);color:var(--text-dark)}

.safety-label{position:absolute;left:61px;top:1085px;width:141px;height:32px;background:var(--ink-teal);
  border-radius:3px;color:var(--white);font-family:"Barlow Condensed",sans-serif;font-weight:600;
  font-size:20px;display:flex;align-items:center;justify-content:center;z-index:2}
.safety-text{position:absolute;left:95px;top:1108px;width:720px;height:68px;background:var(--note-bg);
  border-radius:6px;padding:8px 16px;color:var(--text-dark);font-size:15.5px;line-height:20px}
</style>
</head>
<body>

<!-- Banking -->
<div class="section-band" style="top:43px;font-size:62px">BANKING</div>
<div class="section-icon" style="left:39px;top:24px">
  <div class="disc">
    <svg width="68" height="64" viewBox="0 0 68 64" role="img" aria-label="Bank building icon">
      <g fill="#43b1b8">
        <polygon points="34,2 66,14 2,14"/>
        <rect x="4" y="15" width="60" height="4"/>
        <rect x="7" y="22" width="8" height="28"/><rect x="21" y="22" width="8" height="28"/>
        <rect x="39" y="22" width="8" height="28"/><rect x="53" y="22" width="8" height="28"/>
        <rect x="4" y="52" width="60" height="4"/><rect x="0" y="58" width="68" height="5"/>
      </g>
      <circle cx="34" cy="9" r="3" fill="#fff"/>
    </svg>
  </div>
</div>

<div class="curl" style="top:187px"></div>
<div class="situation" style="top:152px;height:42px">DEBIT AND CREDIT CARDS HAVE STOPPED WORKING (IN STORES; ATMS)</div>
<div class="tab tab-do" style="top:187px">What to do?</div>
<div class="tab tab-refresh" style="top:187px">Refresh when?</div>
<div class="card card-do" style="top:229px;height:70px"><div class="inner">Have $500 in cash available in $20 bills.</div></div>
<div class="card card-refresh" style="top:229px;height:70px"><div class="inner">N/A once done</div></div>

<div class="curl" style="top:379px"></div>
<div class="situation" style="top:325px;height:62px">DEBIT AND CREDIT CARDS HAVE STOPPEDWORKING; YOUR BANK CAN’T ACCESS ITS OWN INFORMATION (ONLINE)</div>
<div class="tab tab-do" style="top:379px">What to do?</div>
<div class="tab tab-refresh" style="top:379px">Refresh when?</div>
<div class="card card-do" style="top:420px;height:336px"><div class="inner">Print paper records of your banking statements that prove what you have in your bank accounts and store it in a safe place in your living space. Ensure it has dates showing and full amounts, as well as your identifiers (name and account numbers) as well as the institution itself (printed screenshots should work fine if your money is in a few accounts requiring many statements). Note the same goes for your liabilities (i.e. be able to prove how much you had left on your mortgage or other bigger loans, if you have such debt).</div></div>
<div class="card card-refresh" style="top:420px;height:76px"><div class="inner">Update this document every 6-12 months</div></div>

<!-- Transportation -->
<div class="section-band" style="top:790px;font-size:62px">TRANSPORTATION</div>
<div class="section-icon" style="left:52px;top:772px">
  <div class="disc">
    <svg width="70" height="66" viewBox="0 0 70 66" role="img" aria-label="Truck icon">
      <g fill="#43b1b8">
        <rect x="8" y="2" width="54" height="52" rx="6"/>
        <rect x="0" y="36" width="70" height="14" rx="3"/>
        <rect x="10" y="52" width="10" height="12" rx="2"/><rect x="50" y="52" width="10" height="12" rx="2"/>
      </g>
      <rect x="15" y="10" width="40" height="14" rx="3" fill="#fff"/>
      <rect x="25" y="36" width="20" height="12" rx="2" fill="#fff"/>
      <g stroke="#43b1b8" stroke-width="1.5"><line x1="28" y1="40" x2="42" y2="40"/><line x1="28" y1="44" x2="42" y2="44"/></g>
      <path d="M4 40 L14 44 L4 44Z M66 40 L56 44 L66 44Z" fill="#fff"/>
    </svg>
  </div>
</div>

<div class="curl" style="top:922px"></div>
<div class="situation" style="top:887px;height:43px">GASSTATIONS HAVE STOPPED WORKING</div>
<div class="tab tab-do" style="top:922px">What to do?</div>
<div class="tab tab-refresh" style="top:922px">Refresh when?</div>
<div class="card card-do" style="top:967px;height:100px"><div class="inner">(If you own a car) Have a standard 40L gas canister filled with gas and available close by in case needed.</div></div>
<div class="card card-refresh" style="top:967px;height:100px"><div class="inner">Use up the gas within 4 months or so, and refill the canister then (i.e. 3 times a year) so that it remains usable</div></div>

<div class="safety-label">SAFETY NOTE:</div>
<div class="safety-text">(If relevant) ensure the can is not in a place where kids can get to it, since it’s not safe for kids to be around gas</div>

</body>
</html>
```